Business Card Design Project for a Restaurant/Wine Bar

New, fresh business card design for Vennica Wine Bar & Restaurant, Bandon, Oregon. We are an established restaurant on the Oregon coast featuring "Italian coastal cuisine."

"Vennica" means bay leaf in Italian. We aren't sure if we would like our logo on the card or not, but if you have something interesting that uses it, then please do so. The basic information is essential - full restaurant name, address, phone and website (do not use www). The font on our menu and wine list may give you some sort of an idea of our style.

One-sided card needed as we often use the backside to write down various types of info for customers.
Updates

After seeing a few submissions, we would like to see what designers can come up with-using the logo, just the leaf, or none at all. Sky is the limit as long as our full restaurant name, address, phone and website (please leave out www) are there. Please contact us if questions!

I appreciate all of your designs! Our deadline is next week, but I will continue to give feedback on designs as I can. This is our busiest season, so my co-owner/chef/husband, won't have time to look at the designs for awhile. When he does, we can make our decision.

cheers,
Maret

Target Market(s)

Fine dining/wine crowd. Would like something simple and elegant, but not pretentious or stuffy. Vennica means bay laurel (bay leaf) in Italian (please see our logo).

Industry/Entity Type

Restaurant

Requirements
Must have
• Full Name of Restaurant: Vennica Wine Bar & Restaurant
Address: 812 Harlow Ave NW, Bandon, Oregon 97408
Phone: 541.608.2937
website: vennicawinebar.com (do not use www)
Should not have
• Loud colors.

```html
<!DOCTYPE html>
<html lang="en">
<head>
<meta charset="utf-8">
<title>Vennica Wine Bar &amp; Restaurant – Business Card</title>
<link href="https://fonts.googleapis.com/css2?family=Lato:wght@400;700&family=Lobster+Two:ital,wght@1,700&display=swap" rel="stylesheet">
<style>
  :root {
    --backdrop: #ece6da;
    --paper-light: #fdf0bf;
    --paper-mid: #f7e3a0;
    --paper-deep: #f0d48a;
    --ink: #3f2a1c;
    --ornament: #6b5647;
    --mark-dot: #8e9a84;
  }
  * { margin: 0; padding: 0; box-sizing: border-box; }
  html, body {
    width: 1200px;
    height: 900px;
    overflow: hidden;
    background: var(--backdrop);
  }
  .canvas {
    width: 1200px;
    height: 900px;
    display: flex;
    align-items: center;
    justify-content: center;
  }
  .business-card {
    position: relative;
    width: 440px;
    height: 770px;
    background:
      radial-gradient(circle at 25% 20%, var(--paper-light) 0%, transparent 45%),
      radial-gradient(circle at 80% 70%, var(--paper-deep) 0%, transparent 50%),
      linear-gradient(160deg, var(--paper-light), var(--paper-mid));
    box-shadow: 0 10px 30px rgba(60, 40, 20, 0.18);
    display: flex;
    flex-direction: column;
    align-items: center;
    text-align: center;
    color: var(--ink);
  }
  .paper-texture {
    position: absolute;
    inset: 0;
  }
  .wordmark {
    position: relative;
    margin-top: 230px;
    display: flex;
    align-items: center;
    gap: 14px;
    font-family: "Lato", sans-serif;
    font-weight: 700;
    font-size: 60px;
    letter-spacing: 1px;
    color: var(--ink);
  }
  .wordmark-dot {
    width: 16px;
    height: 16px;
    border-radius: 50%;
    background: var(--mark-dot);
  }
  .tagline {
    position: relative;
    margin-top: 4px;
    font-family: "Lobster Two", cursive;
    font-style: italic;
    font-weight: 700;
    font-size: 28px;
    color: var(--ink);
  }
  .divider-ornament {
    position: relative;
    margin-top: 26px;
    width: 100px;
    height: 14px;
    border-radius: 7px;
    background: linear-gradient(90deg, transparent, var(--ornament), transparent);
    opacity: 0.7;
  }
  .contact-details {
    position: relative;
    margin-top: 58px;
    font-family: "Lato", sans-serif;
    font-weight: 400;
    font-size: 25px;
    line-height: 1.2;
    font-style: normal;
  }
  .website {
    position: relative;
    margin-top: 74px;
    font-family: "Lato", sans-serif;
    font-weight: 700;
    font-size: 26px;
  }
</style>
</head>
<body>
<main class="canvas">
  <article class="business-card">
    <svg class="paper-texture" role="img" aria-label="Aged parchment texture" width="440" height="770" viewBox="0 0 440 770">
      <defs>
        <radialGradient id="parchment-blot" cx="50%" cy="50%" r="50%">
          <stop offset="0%" stop-color="#ecc978" stop-opacity="0.35"/>
          <stop offset="100%" stop-color="#ecc978" stop-opacity="0"/>
        </radialGradient>
      </defs>
      <rect width="440" height="770" fill="url(#parchment-blot)" opacity="0.6"/>
    </svg>

    <h1 class="wordmark"><span class="wordmark-dot"></span>Vennica</h1>
    <p class="tagline">Wine Bar &amp; Restaurant</p>
    <div class="divider-ornament" role="img" aria-label="Decorative scroll flourish"></div>

    <address class="contact-details">
      812 Harlow Ave NW, Bandon,<br>
      Oregon 97408<br>
      541.608.2937
    </address>
    <p class="website">vennicawinebar.com</p>
  </article>
</main>
</body>
</html>
```